Why Use Me?

Need to create several flyers to promote myself and various home mortgage loan products. I am a loan officer within a larger company so I'm looking for an attractive flyer frame that incorporates my company's colors & logo BUT it has my own custom look and feel. Once this frame is created, I'll have several ideas for body filler. I'm looking for a logo or moniker for myself, synonymous with my business.

```html
<!DOCTYPE html>
<html lang="en">
<head>
<meta charset="UTF-8">
<title>Why Choose Me? – Marcus T. Halden</title>
<link href="https://fonts.googleapis.com/css2?family=Poppins:ital,wght@0,400;0,500;0,600;0,700;0,800;0,900;1,400&display=swap" rel="stylesheet">
<style>
  :root {
    --page-bg: #e4e2e2;
    --sheet: #ededee;
    --ink: #0d0d0f;
    --brand-blue: #4a69a9;
    --bar: #dcdcde;
    --bar-shadow: rgba(0,0,0,0.10);
    --white: #ffffff;
    --photo-top: #d3d3d6;
    --photo-bottom: #2b2b30;
    --figure-a: #c9c9d6;
    --figure-b: #2a2a46;
  }
  * { box-sizing: border-box; margin: 0; padding: 0; }
  html, body {
    width: 1135px; height: 1200px; overflow: hidden;
    background: var(--page-bg);
    font-family: "Poppins", sans-serif;
  }
  .flyer {
    position: absolute; left: 174px; top: 36px;
    width: 788px; height: 1127px;
    background: var(--sheet);
    box-shadow: 0 10px 30px rgba(0,0,0,0.15);
    overflow: hidden;
  }
  .headline {
    position: absolute; left: 66px; top: 66px;
    font-weight: 800; font-size: 86px; line-height: 87px;
    letter-spacing: -1px; color: var(--ink);
  }
  .headline .accent { color: var(--brand-blue); display: block; }
  .agent-name {
    position: absolute; left: 70px; top: 352px;
    font-weight: 600; font-size: 44px; color: var(--ink);
    letter-spacing: -0.5px;
  }
  .figure-art {
    position: absolute; left: 45px; top: 438px;
    width: 128px; height: 468px;
    background: linear-gradient(180deg, var(--figure-a) 0%, var(--figure-b) 40%, var(--figure-b) 100%);
    border-radius: 40px 40px 8px 8px;
    opacity: 0.9;
  }
  .benefits { position: absolute; left: 0; top: 452px; width: 469px; list-style: none; }
  .benefits li {
    position: absolute; left: 180px; width: 289px; height: 50px;
    background: var(--bar);
    box-shadow: 0 4px 4px var(--bar-shadow);
    display: flex; align-items: center;
    padding-left: 21px;
    font-size: 16px; line-height: 19px; color: var(--ink);
  }
  .brand {
    position: absolute; left: 72px; top: 955px;
    display: flex; align-items: center; gap: 12px;
    font-weight: 600; font-size: 27px; color: var(--brand-blue);
  }
  .brand .mark { width: 18px; height: 18px; background: var(--brand-blue); }
  .links {
    position: absolute; left: 72px; top: 1034px;
    font-weight: 500; font-size: 20px; line-height: 25px; color: var(--ink);
  }
  .portrait {
    position: absolute; left: 469px; top: 0; width: 298px; height: 423px;
    background: radial-gradient(circle at 50% 44%, #bfbfc3 0 34%, transparent 35%),
                linear-gradient(180deg, var(--photo-top) 0%, var(--photo-top) 55%, var(--photo-bottom) 100%);
  }
  .side-panel {
    position: absolute; left: 469px; top: 423px; width: 298px; height: 704px;
    background: var(--brand-blue); color: var(--white);
  }
  .edge-strip { position: absolute; left: 767px; top: 0; width: 21px; height: 1127px; background: #f4f4f5; }
  .quote-mark {
    position: absolute; left: 30px; top: 4px;
    font-weight: 900; font-size: 110px; line-height: 1;
  }
  .quote-text {
    position: absolute; left: 26px; top: 120px; width: 236px;
    font-weight: 600; font-size: 24px; line-height: 32px;
  }
  .panel-title {
    position: absolute; left: 28px; top: 296px;
    font-weight: 800; font-size: 24px; letter-spacing: -0.3px;
  }
  .panel-body {
    position: absolute; left: 28px; top: 343px; width: 246px;
    font-style: italic; font-size: 14.3px; line-height: 17.4px;
  }
</style>
</head>
<body>
  <main class="flyer">
    <h1 class="headline">WHY<br>CHOOSE<span class="accent">ME?</span></h1>
    <h2 class="agent-name">Marcus T. Halden</h2>

    <div class="figure-art" role="img" aria-label="Flat illustration of a man in a dark jacket standing beside the list"></div>
    <ul class="benefits">
      <li style="top:0">I'm 17 years at the same<br>exact mortgage company</li>
      <li style="top:66px">Very knowledgeable</li>
      <li style="top:132px">Above and beyond service<br>and availability</li>
      <li style="top:198px">Conversion of tough loans</li>
      <li style="top:264px">“Build a Buyer” program</li>
      <li style="top:330px">Excellent follow-up</li>
      <li style="top:396px">I work with a seasoned<br>lending team</li>
    </ul>

    <div class="brand"><span class="mark"></span><span>Crestline Home Lending</span></div>
    <p class="links">www.crestlinehome.com<br>www.mhalden.crestlinehome.com</p>

    <div class="portrait" role="img" aria-label="Portrait photo of the loan officer in a dark suit and blue tie"></div>

    <aside class="side-panel">
      <div class="quote-mark">“</div>
      <p class="quote-text">I'm In The Office All Day, Every Day And Am Ready To Help You!</p>
      <h3 class="panel-title">LOREM IPSUM</h3>
      <p class="panel-body">Lorem ipsum dolor sit amet, consectetuer adipiscing elit, sed diam nonummy nibh euismod tincidunt ut laoreet dolore magna aliquam erat volutpat. Ut wisi enim ad minim veniam, quis nostrud exerci tation ullamcorper suscipit lobortis nisl ut aliquip ex ea commodo consequat. Duis autem vel eum iriure dolor in hendrerit in vulputate velit esse molestie consequat, vel illum dolore eu feugiat nulla facilisis at vero eros et accumsan et iusto odio dignissim qui blandit praesent luptatum zzril delenit augue duis dolore te feugait nulla facilisi.</p>
    </aside>
    <div class="edge-strip"></div>
  </main>
</body>
</html>
```